Velborne Systems needs a business card

The logo we have uploaded is going to be the image centered on the back.
The business card color is going to be black. Increase the contrast in the logo and lettering so the grey stands out from the black and is more readable. Keep the shadow effect if you can.
On the front, the only part of the logo that should be used is the Egyptian character. We would like the following information included: Name (first last), Title, Phone number, email and company name (Velborne Systems).
The images of colored sound waves we uploaded is a concept we would like implemented on the front as well but please do not use the exact image. It is for guideline purposes.
Get creative with the empty space. We are a technology company that deals with sound and lights. Please not too busy.
Thank you, we look forward to all your submissions.

```html
<!DOCTYPE html>
<html lang="en">
<head>
<meta charset="utf-8">
<title>Velborne Systems — Business Card</title>
<link href="https://fonts.googleapis.com/css2?family=Open+Sans:wght@400;600;700&display=swap" rel="stylesheet">
<style>
  :root {
    --stage: #2b2b2b;
    --card-black: #050505;
    --card-white: #ffffff;
    --brand-red: #e8383d;
    --ink-dark: #2a2a2a;
    --ink-mid: #4a4a4a;
    --rule: #a9a9a9;
  }
  * { box-sizing: border-box; margin: 0; padding: 0; }
  html, body {
    width: 1200px; height: 900px; overflow: hidden;
    background: var(--stage);
    font-family: "Open Sans", Arial, sans-serif;
  }
  .sheet {
    width: 1200px; height: 900px;
    display: flex; justify-content: center; align-items: center; gap: 80px;
  }
  .card {
    position: relative;
    width: 380px; height: 640px;
    border-radius: 22px;
    background: var(--card-black);
    overflow: hidden;
  }
  .brand {
    display: flex; align-items: center; justify-content: center; gap: 12px;
  }
  .brand-mark { width: 22px; height: 22px; background: var(--brand-red); flex: none; }
  .brand-name {
    font-weight: 700; color: var(--brand-red);
    font-size: 26px; letter-spacing: 0.5px; white-space: nowrap;
  }
  /* Front */
  .front-top {
    position: absolute; left: 0; top: 0; width: 100%; height: 280px;
  }
  .front-top .brand { position: absolute; left: 0; right: 0; top: 110px; }
  .sound-band {
    position: absolute; left: 0; width: 100%; top: 170px; height: 110px;
    background: radial-gradient(ellipse at 50% 60%, rgba(90,90,90,0.5), rgba(20,20,20,0) 70%);
  }
  .front-info {
    position: absolute; left: 0; top: 280px; width: 100%; height: 285px;
    background: var(--card-white);
    text-align: center; padding-top: 52px;
  }
  .front-info .notch {
    position: absolute; top: -1px; left: 50%; transform: translateX(-50%);
  }
  .divider {
    width: 190px; height: 1px; margin: 0 auto;
    background: linear-gradient(90deg, transparent, var(--rule), transparent);
  }
  .holder-name {
    font-weight: 700; font-size: 24px; color: var(--ink-dark);
    letter-spacing: 0.3px; margin-top: 10px; line-height: 1.2;
  }
  .holder-title { font-size: 15px; color: var(--ink-mid); margin-top: 2px; }
  .divider.lower { margin-top: 18px; }
  .contact-list {
    list-style: none; margin-top: 22px;
    font-size: 15px; color: var(--ink-dark); line-height: 1.35;
  }
  /* Back */
  .back { display: flex; align-items: center; justify-content: center; }
  .back .brand { margin-top: -40px; }
  .back .brand-name { font-size: 30px; }
  .back .brand-mark { width: 26px; height: 26px; }
</style>
</head>
<body>
<main class="sheet">
  <section class="card front">
    <div class="front-top">
      <div class="sound-band" role="img" aria-label="Faint grey sound wave graphic"></div>
      <div class="brand">
        <span class="brand-mark"></span>
        <span class="brand-name">Velborne Systems</span>
      </div>
    </div>
    <div class="front-info">
      <svg class="notch" width="26" height="14" viewBox="0 0 26 14" aria-hidden="true">
        <polygon points="0,0 26,0 13,14" fill="#050505"/>
      </svg>
      <div class="divider"></div>
      <p class="holder-name">YOUR NAME</p>
      <p class="holder-title">Title</p>
      <div class="divider lower"></div>
      <ul class="contact-list">
        <li>O:(03) 5550 1742</li>
        <li>info@velbornesystems.com</li>
        <li>www.velbornesystems.com</li>
      </ul>
    </div>
  </section>
  <section class="card back">
    <div class="brand">
      <span class="brand-mark"></span>
      <span class="brand-name">Velborne Systems</span>
    </div>
  </section>
</main>
</body>
</html>
```